Do i have coronavirus, flue or cold?

Using information from QRV and government agencies we want to make a easy to read infographic helping patients see if they have coronavirus, the flu or a cold. Using a flow diagram or whatever you think will make it easy to read and digest for the average lamen.

Information is in the word document and in the chart.

We are www.tovipharm.co.uk attached is our brand guidelines, we will be putting this infographic on our website and email/sms it to all of our 300,000 patients.

```html
<!DOCTYPE html>
<html lang="en">
<head>
<meta charset="utf-8">
<title>Do I have Coronavirus, Flue or Cold? – Tovi Pharm</title>
<link href="https://fonts.googleapis.com/css2?family=Nunito:wght@400;600;700;800&family=Didact+Gothic&display=swap" rel="stylesheet">
<style>
  :root {
    --page-bg: #0e1133;
    --card-bg: #ffffff;
    --brand-blue: #3d46a0;
    --brand-blue-soft: #6f82c4;
    --ink: #1b1b2b;
    --cell-bg: #eaf5f6;
    --covid-strong: #f15f24;
    --covid-mid: #f5a281;
    --covid-light: #fad6c4;
    --white: #ffffff;
  }
  * { box-sizing: border-box; margin: 0; padding: 0; }
  html, body { width: 983px; height: 1200px; overflow: hidden; }
  body { background: var(--page-bg); font-family: "Nunito", sans-serif; position: relative; }

  .poster {
    position: absolute; left: 167px; top: 61px;
    width: 650px; height: 1070px;
    background: var(--card-bg);
  }

  .brand {
    position: absolute; left: 29px; top: 44px;
    display: flex; align-items: center; gap: 10px;
  }
  .brand-dot { width: 36px; height: 36px; border-radius: 50%; background: var(--brand-blue); }
  .brand-name {
    font-family: "Nunito", sans-serif; font-weight: 700;
    font-size: 26px; line-height: 26px; color: var(--brand-blue);
  }

  .title {
    position: absolute; right: 22px; top: 30px;
    text-align: right; color: var(--brand-blue);
    font-family: "Didact Gothic", sans-serif;
    font-size: 40px; line-height: 49px; font-weight: 400;
  }

  .hero-band {
    position: absolute; left: 21px; top: 148px;
    width: 613px; height: 115px;
    background: var(--covid-strong);
  }
  .hero-art {
    position: absolute; left: 21px; top: 113px;
    width: 155px; height: 150px;
    background: linear-gradient(160deg, #eef4f8 0%, #eef4f8 45%, var(--brand-blue) 46%, var(--brand-blue) 100%);
    clip-path: polygon(25% 0, 75% 0, 100% 100%, 0 100%, 0 35%);
  }
  .hero-heading {
    position: absolute; right: 29px; top: 154px;
    font-family: "Didact Gothic", sans-serif;
    font-size: 18px; color: var(--white);
  }
  .hero-text {
    position: absolute; right: 29px; top: 187px; width: 460px;
    font-family: "Didact Gothic", sans-serif;
    font-size: 11.6px; line-height: 14px; color: var(--white);
    text-align: justify; text-align-last: right;
  }

  .symptom-table {
    position: absolute; left: 21px; top: 274px;
    display: grid;
    grid-template-columns: 202px 139px 77px 178px;
    grid-template-rows: 52px repeat(8, 80.4px);
    column-gap: 5.5px; row-gap: 6.6px;
  }
  .head {
    background: var(--brand-blue); color: var(--white);
    font-weight: 600; font-size: 25px;
    display: flex; align-items: center; justify-content: center;
  }
  .symptom {
    background: var(--cell-bg);
    display: flex; align-items: center; gap: 13px; padding-left: 14px;
  }
  .symptom-icon {
    flex: none; width: 50px; height: 50px; border-radius: 50%;
    background: var(--covid-strong);
  }
  .symptom-name { font-weight: 700; font-size: 21px; line-height: 25px; color: var(--ink); }

  .cell {
    background: var(--cell-bg);
    text-align: center; padding-top: 14px;
  }
  .answer { display: block; font-weight: 700; font-size: 20.5px; line-height: 24px; color: var(--brand-blue); }
  .note { display: block; margin-top: 3px; font-family: "Didact Gothic", sans-serif; font-size: 10.5px; line-height: 12.6px; color: var(--ink); }
  .covid-strong { background: var(--covid-strong); }
  .covid-mid { background: var(--covid-mid); }
  .covid-light { background: var(--covid-light); }

  .site-url {
    position: absolute; right: 17px; top: 1035px;
    font-family: "Didact Gothic", sans-serif; font-size: 12px; color: var(--brand-blue);
  }
</style>
</head>
<body>
<main class="poster">
  <div class="brand">
    <span class="brand-dot"></span>
    <span class="brand-name">Tovi<br>Pharm</span>
  </div>

  <h1 class="title">Do I have Coronavirus,<br>Flue or Cold?</h1>

  <section class="hero">
    <div class="hero-band"></div>
    <div class="hero-art" role="img" aria-label="Illustration of a man wrapped in a blanket, feeling unwell with a fever"></div>
    <h2 class="hero-heading">Coronavirus symptoms</h2>
    <p class="hero-text">The most common symptoms of COVID-19 are fever, tiredness, and dry cough. Some patients may have aches and pains, nasal congestion, runny nose, sore throat or diarrhoea. These symptoms are usually mild and begin gradually. Some people become infected but don’t develop any symptoms and don't feel unwell.</p>
  </section>

  <section class="symptom-table">
    <div class="head">Symptom</div>
    <div class="head">Flu</div>
    <div class="head">Cold</div>
    <div class="head">Coronavirus</div>

    <div class="symptom"><span class="symptom-icon" role="img" aria-label="Thermometer icon"></span><span class="symptom-name">Fever</span></div>
    <div class="cell"><span class="answer">Yes</span><span class="note">Fever/feeling<br>feverish/chills</span></div>
    <div class="cell"><span class="answer">Yes</span><span class="note">A raised<br>temperature</span></div>
    <div class="cell covid-strong"><span class="answer">Yes</span></div>

    <div class="symptom"><span class="symptom-icon" role="img" aria-label="Illustration of a person coughing"></span><span class="symptom-name">Cough</span></div>
    <div class="cell"><span class="answer">Yes</span></div>
    <div class="cell"><span class="answer">Yes</span></div>
    <div class="cell covid-strong"><span class="answer">Yes</span><span class="note">Dry cough</span></div>

    <div class="symptom"><span class="symptom-icon" role="img" aria-label="Illustration of a tired person"></span><span class="symptom-name">Tiredness</span></div>
    <div class="cell"><span class="answer">Yes</span><span class="note">Fatigue</span></div>
    <div class="cell"><span class="answer">Mild</span></div>
    <div class="cell covid-strong"><span class="answer">Yes</span></div>

    <div class="symptom"><span class="symptom-icon" role="img" aria-label="Illustration of an aching arm"></span><span class="symptom-name">Muscle<br>Aches</span></div>
    <div class="cell"><span class="answer">Yes</span><span class="note">Muscle or<br>body aches</span></div>
    <div class="cell"><span class="answer">Yes</span></div>
    <div class="cell covid-strong"><span class="answer">Yes</span><span class="note">Aches and pains</span></div>

    <div class="symptom"><span class="symptom-icon" role="img" aria-label="Illustration of a person with a sore throat"></span><span class="symptom-name">Sore<br>Throat</span></div>
    <div class="cell"><span class="answer">Yes</span></div>
    <div class="cell"><span class="answer">Yes</span></div>
    <div class="cell covid-mid"><span class="answer">Sometimes</span><span class="note">Dry cough</span></div>

    <div class="symptom"><span class="symptom-icon" role="img" aria-label="Illustration of a person with a headache"></span><span class="symptom-name">Headache</span></div>
    <div class="cell"><span class="answer">Yes</span></div>
    <div class="cell"><span class="answer">Rare</span></div>
    <div class="cell covid-mid"><span class="answer">Sometimes</span></div>

    <div class="symptom"><span class="symptom-icon" role="img" aria-label="Illustration of a person with stomach upset"></span><span class="symptom-name">Diarrhoea</span></div>
    <div class="cell"><span class="answer">Sometimes</span><span class="note">More common<br>in children</span></div>
    <div class="cell"><span class="answer">No</span></div>
    <div class="cell covid-mid"><span class="answer">Sometimes</span></div>

    <div class="symptom"><span class="symptom-icon" role="img" aria-label="Illustration of a person with a runny nose"></span><span class="symptom-name">Runny<br>nose</span></div>
    <div class="cell"><span class="answer">Yes</span><span class="note">A blocked or<br>runny nose</span></div>
    <div class="cell"><span class="answer">Yes</span><span class="note">Runny or<br>stuffy nose</span></div>
    <div class="cell covid-light"><span class="answer">Rare</span><span class="note">Nasal congestion</span></div>
  </section>

  <p class="site-url">www.tovipharm.co.uk</p>
</main>
</body>
</html>
```